I need some facebook page ads designed

We need some facebook optimized graphics to post on our page for new insurance quotes on home and auto insurance

```html
<!DOCTYPE html>
<html lang="en">
<head>
<meta charset="utf-8">
<title>Norvale Insurance Agency – Home &amp; Auto Quotes</title>
<link rel="stylesheet" href="https://fonts.googleapis.com/css2?family=Open+Sans:wght@300;400;700;800&family=Roboto+Condensed:wght@400&family=Roboto:wght@400&display=swap">
<style>
  :root {
    --plum-light: #8a3659;
    --plum-dark: #55293d;
    --plum-text: #5a2a40;
    --ink: #2a2a2a;
    --black: #050505;
    --paper-top: #f7f7f7;
    --paper-bottom: #e6e6e6;
    --white: #ffffff;
    --hatch-grey: #d6d6d6;
    --photo-sky: #e9eef0;
    --photo-mid: #c9d3d8;
    --photo-green: #6f8a6a;
  }
  * { margin: 0; padding: 0; box-sizing: border-box; }
  html, body {
    width: 1200px; height: 1200px; overflow: hidden;
    background: var(--paper-bottom);
  }
  .ad {
    position: relative; width: 1200px; height: 1200px; overflow: hidden;
    background: linear-gradient(180deg, var(--paper-top) 0%, var(--paper-bottom) 100%);
    font-family: "Open Sans", Arial, sans-serif;
  }
  .ad__shapes { position: absolute; inset: 0; }
  .headline {
    position: absolute; left: 62px; top: 120px;
    color: var(--white); font-size: 41px; line-height: 57px;
    font-weight: 300; letter-spacing: 0.2px; text-transform: uppercase;
  }
  .headline strong { font-weight: 800; }
  .quote-button {
    position: absolute; left: 71px; top: 441px; width: 249px; height: 64px;
    background: linear-gradient(180deg, #3a3a3a 0%, var(--black) 45%);
    border: 2px solid #000; border-radius: 10px;
    color: var(--white); font-weight: 700; font-size: 28px;
    display: flex; align-items: center; justify-content: center;
    text-decoration: none;
  }
  .tagline {
    position: absolute; left: 60px; top: 784px;
    font-family: "Roboto Condensed", "Arial Narrow", sans-serif;
    font-size: 40px; color: var(--ink); letter-spacing: -0.5px;
  }
  .brand {
    position: absolute; left: 95px; top: 850px; width: 330px;
    color: var(--ink); text-align: center;
  }
  .brand__name {
    display: flex; align-items: center; justify-content: center; gap: 14px;
    font-size: 76px; font-weight: 700; line-height: 1; letter-spacing: -1px;
  }
  .brand__mark { width: 22px; height: 22px; background: var(--ink); }
  .brand__type {
    margin-top: 12px; font-family: "Roboto", Arial, sans-serif;
    font-size: 17px; letter-spacing: 1px;
  }
  .brand__lines {
    font-family: "Roboto", Arial, sans-serif; font-size: 13px; margin-top: 2px;
  }
  .web-address {
    position: absolute; left: 61px; top: 1088px;
    font-size: 35px; color: var(--ink); font-weight: 400;
  }
  .web-address b { color: var(--plum-text); font-weight: 700; }
</style>
</head>
<body>
<main class="ad">
  <svg class="ad__shapes" width="1200" height="1200" viewBox="0 0 1200 1200" aria-hidden="false">
    <defs>
      <linearGradient id="plumFill" x1="0" y1="0" x2="1" y2="1">
        <stop offset="0" stop-color="var(--plum-light)"/>
        <stop offset="1" stop-color="var(--plum-dark)"/>
      </linearGradient>
      <radialGradient id="photoFill" cx="0.45" cy="0.55" r="0.7">
        <stop offset="0" stop-color="var(--photo-sky)"/>
        <stop offset="0.6" stop-color="var(--photo-mid)"/>
        <stop offset="1" stop-color="var(--photo-green)"/>
      </radialGradient>
      <clipPath id="canvasClip"><rect width="1200" height="1200"/></clipPath>
    </defs>
    <g clip-path="url(#canvasClip)">
      <circle class="plum-disc" cx="275" cy="278" r="421" fill="url(#plumFill)"/>
      <circle class="hatch-disc" cx="1164" cy="167" r="120" fill="var(--hatch-grey)"/>
      <circle class="accent-disc" cx="1182" cy="342" r="88" fill="var(--black)"/>
      <circle class="black-disc" cx="982" cy="1025" r="445" fill="var(--black)"/>
      <circle class="frame-ring" cx="855" cy="640" r="397" fill="none" stroke="var(--white)" stroke-width="2"/>
      <circle class="home-photo" cx="855" cy="640" r="385" fill="url(#photoFill)"
              role="img" aria-label="Photo of a small model house with a grey roof, red chimney and a set of keys hanging from it, on a green lawn base"/>
    </g>
  </svg>

  <h1 class="headline">
    We help<br>
    <strong>consumers save money,</strong><br>
    we help <strong>families protect</strong><br>
    and preserve their<br>
    <strong>financial future.</strong>
  </h1>

  <a class="quote-button" href="#">Get a Quote</a>

  <p class="tagline">SIMPLE. HAPPY. INSURED.</p>

  <div class="brand">
    <div class="brand__name"><span class="brand__mark"></span>norvale</div>
    <div class="brand__type">INSURANCE AGENCY</div>
    <div class="brand__lines">Auto | Home | Life | Business</div>
  </div>

  <p class="web-address">www.<b>insurenorvale</b>.com</p>
</main>
</body>
</html>
```